Stationary Design for Stunning new Logo

I need to envelopes, letterhead, business cards designed to compliment our new logo.

We are a 25 year old printing company going through a brand refresh. All items should have the design extended to both sides for full print ability.

Industry/Entity Type

Printing

Requirements
Must have
• It must utilize the new logo & colors PMS 300 & PMS 295.

```html
<!DOCTYPE html>
<html lang="en">
<head>
<meta charset="utf-8">
<title>Inkwell Stationery Set</title>
<link href="https://fonts.googleapis.com/css2?family=Michroma&family=Roboto+Condensed:wght@400&family=Roboto:wght@400&display=swap" rel="stylesheet">
<style>
  :root{
    --bright-blue:#1f7ff2;
    --navy:#0c1760;
    --paper:#ffffff;
    --backdrop:#a6b1b8;
    --backdrop-edge:#7b8d98;
    --shadow:#c9c9c9;
  }
  *{margin:0;padding:0;box-sizing:border-box}
  html,body{width:1200px;height:1000px;overflow:hidden}
  body{
    position:relative;
    background:radial-gradient(ellipse at 45% 45%, #c4cacd 0%, var(--backdrop) 45%, var(--backdrop-edge) 100%);
    font-family:"Roboto", Arial, sans-serif;
  }
  .sheet{position:absolute;background:var(--paper);overflow:hidden}
  .sheet--shadowed{box-shadow:4px 4px 0 var(--shadow)}

  .brand-ring{position:absolute;overflow:visible}
  .brand-ring circle{fill:none;stroke:var(--navy)}

  .brand-vertical{
    position:absolute;
    writing-mode:vertical-rl;
    font-family:"Michroma", sans-serif;
    color:var(--navy);
    line-height:1;
    white-space:nowrap;
  }
  .tagline{
    position:absolute;
    font-family:"Roboto Condensed", Arial, sans-serif;
    color:var(--bright-blue);
    white-space:nowrap;
    text-transform:uppercase;
  }

  /* letterhead */
  .letterhead--back{left:100px;top:208px;width:470px;height:622px}
  .letterhead--back .edge-band{position:absolute;left:-8px;top:587px;width:16px;height:35px;background:var(--navy)}
  .letterhead--front{left:55px;top:170px;width:480px;height:622px}
  .letterhead .brand-ring{left:0;top:0;width:110px;height:110px}
  .letterhead .brand-vertical{left:-4px;top:126px;font-size:58px;letter-spacing:19px}
  .letterhead .tagline{right:4px;bottom:10px;font-size:7.5px}
  .letterhead--back .tagline{bottom:8px;right:25px}

  /* envelope */
  .envelope--back{left:650px;top:190px;width:495px;height:272px}
  .envelope--front{left:607px;top:170px;width:496px;height:270px}
  .envelope .flap-line{position:absolute;left:0;right:0;top:58px;border-top:1px solid #e6e6e6}
  .envelope .brand-ring{left:0;top:0;width:160px;height:190px}
  .envelope .tagline{left:163px;top:24px;font-size:5.5px;transform:rotate(180deg)}
  .envelope .brand-name{
    position:absolute;left:8px;top:94px;
    font-family:"Michroma", sans-serif;font-size:14px;color:var(--navy);letter-spacing:.5px;
  }

  /* business cards */
  .card{top:561px;width:112px;height:196px}
  .card--contact{left:677px}
  .card--name{left:819px}
  .card--contact .brand-ring{left:0;top:0;width:45px;height:45px}
  .card--contact .brand-vertical{left:-1px;top:49px;font-size:17px;letter-spacing:5px}
  .contact-block{
    position:absolute;right:6px;top:77px;
    text-align:right;font-size:5px;line-height:6px;color:var(--navy);
  }
  .contact-block p + p{margin-top:4px}
  .card--contact .tagline{left:28px;bottom:5px;font-size:3.5px}
  .card--name .brand-ring{left:0;top:0;width:112px;height:160px}
  .card-person{
    position:absolute;left:0;right:0;top:85px;text-align:center;
    font-family:"Roboto", Arial, sans-serif;color:var(--navy);
  }
  .card-person .person-name{font-size:11px;line-height:12px}
  .card-person .person-role{font-size:10px;line-height:11px}
  .card--name .brand-name{
    position:absolute;left:0;right:0;bottom:0;text-align:center;
    font-family:"Michroma", sans-serif;font-size:15px;line-height:17px;color:var(--navy);
    white-space:nowrap;
  }
</style>
</head>
<body>

  <section class="letterhead letterhead--back sheet">
    <div class="edge-band"></div>
    <p class="tagline">Outstanding service • Quality product • Competitive pricing.</p>
  </section>

  <section class="letterhead letterhead--front sheet sheet--shadowed">
    <svg class="brand-ring" viewBox="0 0 110 110" aria-hidden="true">
      <circle cx="50" cy="50" r="46" stroke-width="6"/>
    </svg>
    <h1 class="brand-vertical">INKWELL</h1>
    <p class="tagline">Outstanding service • Quality product • Competitive pricing.</p>
  </section>

  <section class="envelope envelope--back sheet"></section>

  <section class="envelope envelope--front sheet sheet--shadowed">
    <div class="flap-line"></div>
    <svg class="brand-ring" viewBox="0 0 160 190" aria-hidden="true">
      <circle cx="73" cy="100" r="78" stroke-width="8"/>
    </svg>
    <p class="tagline">Outstanding service • Quality product • Competitive pricing</p>
    <p class="brand-name">INKWELL</p>
  </section>

  <section class="card card--contact sheet sheet--shadowed">
    <svg class="brand-ring" viewBox="0 0 45 45" aria-hidden="true">
      <circle cx="21" cy="21" r="18" stroke-width="3"/>
    </svg>
    <p class="brand-vertical">INKWELL</p>
    <div class="contact-block">
      <p>xx address street, country</p>
      <p>+xx- phone number<br>+xx- fax number</p>
      <p>email@inkwellprint.com<br>www.inkwellprint.com</p>
    </div>
    <p class="tagline">Outstanding service • Quality product • Competitive pricing</p>
  </section>

  <section class="card card--name sheet sheet--shadowed">
    <svg class="brand-ring" viewBox="0 0 112 160" aria-hidden="true">
      <circle cx="56" cy="90" r="68" stroke-width="6"/>
    </svg>
    <div class="card-person">
      <p class="person-name">Alex Carter</p>
      <p class="person-role">CEO</p>
    </div>
    <p class="brand-name">INKWELL</p>
  </section>

</body>
</html>
```